Business Cards

The name of our firm is "Bayfield Insurance adjusters"
We separate ourselves from all other public adjusters because most of us worked for the insurance companies so we understand their games.
As Insurance adjusters we represent the Insured, not the insurance companies. Our # 1 priority is to handle the entire claim process as seamless as possible on behalf of the homeowner/business owner so they don't have to deal with the hassles and headaches. Just as the logo your team designed, I want the cards to stand out from everyone elses. I also want the cards to help better understand our services and Value on hiring us and value that we can offer.
I uploaded the logo whenever I created the project. I don't see an option on re uploading the logo anywhere. Any advise??

```html
<!DOCTYPE html>
<html lang="en">
<head>
<meta charset="utf-8">
<title>Bayfield Insurance Adjusters — Business Cards</title>
<link rel="stylesheet" href="https://fonts.googleapis.com/css2?family=Open+Sans:wght@400;600;700;800&display=swap">
<style>
  :root {
    --backdrop: #2a2a2c;
    --card-white: #ffffff;
    --brand-blue: #1a6fa8;
    --brand-blue-deep: #0d4f7e;
    --back-top: #0f5a88;
    --back-bottom: #1d7bb0;
    --back-mark: #0b4568;
    --ink: #1f1f22;
  }
  * { box-sizing: border-box; margin: 0; padding: 0; }
  html, body {
    width: 1200px; height: 900px; overflow: hidden;
    background: var(--backdrop);
    font-family: "Open Sans", Arial, sans-serif;
  }
  .canvas { position: relative; width: 1200px; height: 900px; }

  .card {
    position: absolute;
    width: 700px; height: 400px;
    left: 250px;
    border-radius: 22px;
    overflow: hidden;
    box-shadow: 0 14px 30px rgba(0,0,0,.45);
  }

  /* Back of card */
  .card-back {
    top: 40px;
    background: linear-gradient(160deg, var(--back-top) 0%, var(--brand-blue-deep) 45%, var(--back-bottom) 100%);
    display: flex; align-items: center; justify-content: center;
  }
  .back-brand {
    display: flex; flex-direction: column; align-items: center;
    color: var(--back-mark); font-weight: 800; text-transform: uppercase;
  }
  .back-brand .brand-name { font-size: 58px; letter-spacing: 2px; line-height: 1; }
  .back-brand .brand-sub { font-size: 17px; letter-spacing: 3px; margin-top: 8px; }

  /* Front of card */
  .card-front {
    top: 470px;
    background: var(--card-white);
    border-bottom: 10px solid var(--brand-blue);
  }
  .front-brand {
    position: absolute; left: 48px; top: 46px;
    display: flex; align-items: center; gap: 12px;
    color: var(--brand-blue); font-weight: 800; text-transform: uppercase;
  }
  .front-brand .brand-dot {
    width: 40px; height: 40px; border-radius: 50%; background: var(--brand-blue);
  }
  .front-brand .brand-text { display: flex; flex-direction: column; line-height: 1; }
  .front-brand .brand-name { font-size: 36px; letter-spacing: 1px; }
  .front-brand .brand-sub { font-size: 11px; letter-spacing: 2px; margin-top: 6px; }

  .person {
    position: absolute; right: 42px; top: 128px; text-align: right;
  }
  .person-name {
    color: var(--brand-blue); font-weight: 700; font-size: 32px;
    letter-spacing: 2px; text-transform: uppercase; line-height: 1.1;
  }
  .person-title { color: var(--ink); font-size: 20px; margin-top: 2px; }
  .title-bar {
    position: absolute; right: 0; top: 138px;
    width: 10px; height: 58px; background: var(--brand-blue);
  }

  .contacts {
    position: absolute; left: 48px; bottom: 48px;
    list-style: none; color: var(--ink); font-size: 21px;
  }
  .contacts li { display: flex; align-items: center; gap: 14px; margin-top: 10px; }
  .contacts svg { width: 20px; height: 20px; flex: none; fill: var(--brand-blue); }
</style>
</head>
<body>
<main class="canvas">

  <section class="card card-back" aria-label="Card back">
    <div class="back-brand">
      <span class="brand-name">Bayfield</span>
      <span class="brand-sub">Insurance Adjusters</span>
    </div>
  </section>

  <section class="card card-front" aria-label="Card front">
    <div class="front-brand">
      <span class="brand-dot"></span>
      <span class="brand-text">
        <span class="brand-name">Bayfield</span>
        <span class="brand-sub">Insurance Adjusters</span>
      </span>
    </div>

    <div class="person">
      <p class="person-name">Daniel Reyes</p>
      <p class="person-title">Founder/CEO</p>
    </div>
    <span class="title-bar"></span>

    <ul class="contacts">
      <li>
        <svg viewBox="0 0 24 24" aria-hidden="true"><path d="M6.6 10.8a15 15 0 0 0 6.6 6.6l2.2-2.2a1 1 0 0 1 1-.25 11.4 11.4 0 0 0 3.6.57 1 1 0 0 1 1 1V20a1 1 0 0 1-1 1A17 17 0 0 1 3 4a1 1 0 0 1 1-1h3.5a1 1 0 0 1 1 1c0 1.25.2 2.45.57 3.6a1 1 0 0 1-.25 1z"/></svg>
        555-214-7730
      </li>
      <li>
        <svg viewBox="0 0 24 24" aria-hidden="true"><path d="M2 5h20v14H2z M4 7v.4l8 5.2 8-5.2V7z" fill-rule="evenodd"/></svg>
        daniel@bayfieldinsadj.com
      </li>
      <li>
        <svg viewBox="0 0 24 24" aria-hidden="true"><circle cx="12" cy="12" r="10"/></svg>
        www.bayfieldinsadj.com
      </li>
    </ul>
  </section>

</main>
</body>
</html>
```